Business Cards for Valet Parking Company
Modern & Hospitality Oriented
Business Cards for Valet Parking Company - Automotive
Creative Brief
Simple
Colin Marsh
Owner & President
48270 E 9 Pine Avenue Suite 400 Farmington Hills, MI 48127
colin@orbitparkco.com
www.orbitparkco.com
On back of card: Anticipate, Invite & Engage

```html
<!DOCTYPE html>
<html lang="en">
<head>
<meta charset="utf-8">
<title>Orbit Parking Co — Business Cards</title>
<link rel="stylesheet" href="https://fonts.googleapis.com/css2?family=Montserrat:ital,wght@0,400;0,500;0,600;0,700;1,400&display=swap">
<style>
  :root {
    --backdrop: #cfcac6;
    --charcoal: #3b3b3d;
    --sunflower: #f6c512;
    --panel: #f2f2f2;
    --panel-shade: #d9d9d9;
    --ink: #3b3b3d;
    --paper-text: #e9e9e9;
  }
  * { margin: 0; padding: 0; box-sizing: border-box; }
  html, body { width: 1200px; height: 803px; overflow: hidden; }
  body {
    background: var(--backdrop);
    font-family: "Montserrat", sans-serif;
    position: relative;
  }
  .card {
    position: absolute;
    top: 246px;
    width: 540px;
    height: 310px;
    border-radius: 4px;
    overflow: hidden;
    box-shadow: 0 8px 20px rgba(0,0,0,.18);
  }
  .card--front { left: 45px; }
  .card--back { left: 615px; }
  .card svg.card-art { position: absolute; inset: 0; }

  .brand {
    position: absolute;
    right: 42px;
    top: 100px;
    display: flex;
    align-items: center;
    gap: 10px;
  }
  .brand-dot {
    width: 22px; height: 22px;
    background: var(--sunflower);
    border-radius: 50%;
  }
  .brand-name {
    font-weight: 700;
    font-size: 25px;
    letter-spacing: 1px;
    color: var(--ink);
    text-transform: uppercase;
  }
  .website {
    position: absolute;
    right: 58px;
    top: 158px;
    font-size: 14px;
    font-weight: 500;
    color: var(--ink);
  }
  .contact {
    position: absolute;
    left: 22px;
    font-size: 12px;
    color: var(--paper-text);
    line-height: 1.35;
    display: flex;
    gap: 10px;
    align-items: flex-start;
  }
  .contact--phone { top: 204px; }
  .contact--address { top: 246px; }
  .contact svg { flex: none; margin-top: 2px; }
  .email {
    position: absolute;
    right: 30px;
    bottom: 22px;
    font-size: 14px;
    color: var(--paper-text);
    display: flex;
    align-items: center;
    gap: 10px;
  }
  .holder {
    position: absolute;
    right: 28px;
    top: 26px;
    text-align: right;
    color: var(--paper-text);
  }
  .holder-name {
    font-size: 17px;
    font-weight: 600;
    letter-spacing: 1px;
    text-transform: uppercase;
  }
  .holder-role {
    font-size: 11px;
    font-style: italic;
    margin-top: 3px;
  }
  .tagline {
    position: absolute;
    right: 28px;
    bottom: 22px;
    font-size: 13px;
    font-weight: 500;
    letter-spacing: 1px;
    color: var(--sunflower);
  }
</style>
</head>
<body>

  <section class="card card--front" aria-label="Business card front">
    <svg class="card-art" width="540" height="310" viewBox="0 0 540 310" aria-hidden="true">
      <rect width="540" height="310" fill="var(--charcoal)"/>
      <path d="M250 0 H540 V62 H290 Z" fill="var(--sunflower)"/>
      <path d="M0 44 H240 Q262 44 272 66 L284 86 H540 V154 H300 Q286 154 278 168 L266 190 H0 Z" fill="var(--panel-shade)"/>
      <path d="M0 40 H236 Q258 40 268 62 L280 82 H540 V150 H296 Q282 150 274 164 L262 186 H0 Z" fill="var(--panel)"/>
      <rect x="250" y="150" width="270" height="34" rx="17" fill="var(--sunflower)"/>
    </svg>

    <div class="brand">
      <span class="brand-dot"></span>
      <span class="brand-name">Orbit Parking Co</span>
    </div>
    <div class="website">www.orbitparkco.com</div>

    <div class="contact contact--phone">
      <svg width="14" height="14" viewBox="0 0 24 24" aria-hidden="true"><path fill="var(--paper-text)" d="M6.6 10.8a15.1 15.1 0 0 0 6.6 6.6l2.2-2.2a1 1 0 0 1 1-.25 11.4 11.4 0 0 0 3.6.57 1 1 0 0 1 1 1V20a1 1 0 0 1-1 1A17 17 0 0 1 3 4a1 1 0 0 1 1-1h3.5a1 1 0 0 1 1 1c0 1.25.2 2.45.57 3.57a1 1 0 0 1-.25 1z"/></svg>
      <div>248 555 0142<br>248 555 0143</div>
    </div>
    <div class="contact contact--address">
      <svg width="16" height="14" viewBox="0 0 24 22" aria-hidden="true"><path fill="var(--paper-text)" d="M12 1 1 11h3v10h6v-6h4v6h6V11h3z"/></svg>
      <div>48270 E 9 Pine Avenue Suite 400<br>Farmington Hills, MI 48127</div>
    </div>
    <div class="email">
      <svg width="18" height="13" viewBox="0 0 18 13" aria-hidden="true"><rect x="0.75" y="0.75" width="16.5" height="11.5" fill="none" stroke="var(--paper-text)" stroke-width="1.5"/><path d="M1 1l8 6 8-6" fill="none" stroke="var(--paper-text)" stroke-width="1.5"/></svg>
      <span>colin@orbitparkco.com</span>
    </div>
  </section>

  <section class="card card--back" aria-label="Business card back">
    <svg class="card-art" width="540" height="310" viewBox="0 0 540 310" aria-hidden="true">
      <rect width="540" height="310" fill="var(--charcoal)"/>
      <path d="M0 110 H210 Q232 110 242 132 L256 162 Q266 184 290 184 H540 V230 H0 Z" fill="var(--sunflower)"/>
      <path d="M0 104 H206 Q228 104 238 126 L250 152 Q260 174 284 174 H540 V212 H300 Q276 212 266 232 L252 262 H0 Z" fill="var(--panel-shade)"/>
      <path d="M0 100 H202 Q224 100 234 122 L246 148 Q256 170 280 170 H540 V206 H296 Q272 206 262 226 L248 256 H0 Z" fill="var(--panel)"/>
    </svg>
    <div class="holder">
      <div class="holder-name">Colin Marsh</div>
      <div class="holder-role">Owner &amp; President</div>
    </div>
    <div class="tagline">Anticipate, Invite &amp; Engage</div>
  </section>

</body>
</html>
```